Business Card Design

I need a card design for Melbourne based business in Australia, called M P Concrete Services. We Concrete and excavate. Concreteing is main part of business.Commercial ,Residential and industrial.We want to be known as M P C (services) as form of abbreviation.We would like to highlight the initials with contact phone. A clean straight edge design. We have no color preference and would prefer a design that can easily be used on all parts of our business including clothing,vechiles and stationary

Industry/Entity Type

Business

Contact Information for Business Card

Hugh 0491 570 156
Peter 0491 570 157
mpcsercices@quollmail.com

```html
<!DOCTYPE html>
<html lang="en">
<head>
<meta charset="utf-8">
<title>M P Concrete Services – Business Card</title>
<link rel="stylesheet" href="https://fonts.googleapis.com/css2?family=Oswald:wght@400;500;600&display=swap">
<style>
  :root {
    --backdrop: #2a2a2a;
    --card: #ffffff;
    --brand-blue: #1a78c2;
    --ink: #1b1b1b;
    --on-blue: #ffffff;
  }
  * { margin: 0; padding: 0; box-sizing: border-box; }
  html, body {
    width: 1200px;
    height: 586px;
    overflow: hidden;
    background: var(--backdrop);
  }
  .canvas {
    position: relative;
    width: 1200px;
    height: 586px;
    background: var(--backdrop);
  }
  .business-card {
    position: absolute;
    left: 463px;
    top: 53px;
    width: 274px;
    height: 480px;
    background: var(--card);
    font-family: "Oswald", "Arial Narrow", sans-serif;
    color: var(--ink);
  }
  .brand-name {
    position: absolute;
    top: 8px;
    left: 0;
    width: 100%;
    text-align: center;
    font-size: 54px;
    font-weight: 600;
    letter-spacing: 6px;
    line-height: 60px;
    color: var(--brand-blue);
  }
  .brand-mark {
    position: absolute;
    top: 92px;
    left: 67px;
    width: 140px;
    height: 140px;
  }
  .contact-list {
    position: absolute;
    top: 294px;
    left: 0;
    width: 100%;
    list-style: none;
    text-align: center;
  }
  .contact-item {
    font-size: 17px;
    font-weight: 500;
    line-height: 36px;
    white-space: nowrap;
  }
  .contact-name {
    font-size: 13px;
    letter-spacing: 0.5px;
    text-transform: uppercase;
    margin-right: 8px;
  }
  .contact-email {
    font-size: 16px;
    font-weight: 400;
  }
  .company-band {
    position: absolute;
    top: 430px;
    left: 0;
    width: 100%;
    height: 32px;
    background: var(--brand-blue);
    color: var(--on-blue);
    text-align: center;
    font-size: 19px;
    font-weight: 500;
    line-height: 32px;
    letter-spacing: 0.5px;
    text-transform: uppercase;
  }
</style>
</head>
<body>
  <main class="canvas">
    <section class="business-card">
      <div class="brand-name">MPC</div>
      <svg class="brand-mark" viewBox="0 0 140 140" aria-hidden="true">
        <circle cx="70" cy="70" r="70" fill="#1a78c2"/>
      </svg>
      <ul class="contact-list">
        <li class="contact-item"><span class="contact-name">Hugh</span>0491 570 156</li>
        <li class="contact-item"><span class="contact-name">Peter</span>0491 570 157</li>
        <li class="contact-item contact-email">mpcsercices@quollmail.com</li>
      </ul>
      <div class="company-band">M P Concrete Services</div>
    </section>
  </main>
</body>
</html>
```